Billboard design for retail kitchen cabinet business

We have a large 7,000 square-foot showroom of beautiful kitchen cabinet displays of all different designs and price ranges. In business for over 50 years with expert designers.
Full size Halvard Media 14' X 48' billboard
Target Market(s)
Retail public on high traffic Los Angeles streets

```html
<!DOCTYPE html>
<html lang="en">
<head>
<meta charset="utf-8">
<title>Oakmere Kitchens – Billboard</title>
<link href="https://fonts.googleapis.com/css2?family=Montserrat:wght@600;700;800&display=swap" rel="stylesheet">
<style>
  :root {
    --page: #ffffff;
    --ink: #141414;
    --panel: #161616;
    --band: #72695a;
    --band-light: #80765f;
    --white: #ffffff;
    --photo-warm: #b98a5e;
    --photo-light: #e9e2d8;
    --photo-wood: #7a4a2c;
  }
  * { box-sizing: border-box; margin: 0; padding: 0; }
  html, body {
    width: 1071px;
    height: 1200px;
    overflow: hidden;
    background: var(--page);
    font-family: "Montserrat", Arial, sans-serif;
  }
  .canvas {
    position: relative;
    width: 1071px;
    height: 1200px;
  }
  .billboard {
    position: absolute;
    left: 35px;
    top: 454px;
    width: 1000px;
    height: 291px;
    box-shadow: 0 10px 18px rgba(0, 0, 0, 0.28);
    background: var(--white);
  }
  .message-panel {
    position: absolute;
    left: 0;
    top: 0;
    width: 554px;
    height: 229px;
    background: radial-gradient(ellipse at 70% 30%, #262626 0%, var(--panel) 70%);
  }
  .headline {
    position: absolute;
    left: 35px;
    top: 26px;
    color: var(--white);
    font-weight: 700;
    line-height: 1;
    text-transform: uppercase;
  }
  .headline .lead {
    display: block;
    font-size: 44px;
    letter-spacing: 0.5px;
  }
  .headline .middle {
    display: block;
    font-size: 26px;
    font-weight: 600;
    margin: 2px 0 3px;
    letter-spacing: 0.2px;
  }
  .brand-name {
    position: absolute;
    left: 398px;
    top: 66px;
    width: 130px;
    color: var(--white);
    font-weight: 800;
    font-size: 19px;
    line-height: 1.1;
    text-transform: uppercase;
  }
  .phone-pill {
    position: absolute;
    left: 26px;
    top: 158px;
    width: 424px;
    height: 49px;
    background: var(--white);
    border-radius: 25px;
  }
  .phone-icon {
    position: absolute;
    left: -2px;
    top: -3px;
    width: 55px;
    height: 55px;
  }
  .phone-number {
    position: absolute;
    left: 68px;
    top: 4px;
    font-size: 40px;
    font-weight: 700;
    line-height: 41px;
    color: var(--ink);
    letter-spacing: 0.3px;
  }
  .web-band {
    position: absolute;
    left: 0;
    top: 229px;
    width: 554px;
    height: 62px;
    background: linear-gradient(90deg, var(--band) 0%, var(--band-light) 100%);
  }
  .globe-icon {
    position: absolute;
    left: 44px;
    top: 14px;
    width: 34px;
    height: 34px;
  }
  .web-address {
    position: absolute;
    left: 96px;
    top: 13px;
    font-size: 30px;
    font-weight: 700;
    line-height: 36px;
    color: var(--white);
  }
  .showroom-photo {
    position: absolute;
    left: 560px;
    top: 0;
    width: 440px;
    height: 291px;
    background:
      linear-gradient(180deg, var(--photo-light) 0%, var(--photo-light) 18%, transparent 40%),
      linear-gradient(90deg, var(--photo-wood) 0%, var(--photo-warm) 30%, var(--photo-light) 75%, #d8cfc4 100%);
  }
</style>
</head>
<body>
  <main class="canvas">
    <section class="billboard" aria-label="Oakmere Kitchens billboard">
      <div class="message-panel">
        <h1 class="headline">
          <span class="lead">Our Kitchen</span>
          <span class="middle">Showroom is where</span>
          <span class="lead">Dreams Begin!</span>
        </h1>
        <p class="brand-name">Oakmere Kitchens</p>
        <div class="phone-pill">
          <svg class="phone-icon" viewBox="0 0 55 55" aria-hidden="true">
            <circle cx="27.5" cy="27.5" r="25.5" fill="#72695a" stroke="#ffffff" stroke-width="3"/>
            <path d="M20 16c1.5-1 3-.8 3.8.6l2.4 4.2c.7 1.3.3 2.6-.8 3.4l-1.6 1.1c1 2.6 3 4.8 5.6 6.1l1.2-1.5c.9-1.1 2.3-1.3 3.5-.5l4 2.6c1.3.9 1.5 2.4.5 3.8-1.6 2.3-4 3.3-6.6 2.5C24.5 35.9 19.2 30.3 17.3 23.3c-.7-2.8.4-5.6 2.7-7.3z" fill="#ffffff"/>
          </svg>
          <span class="phone-number">(310) 555-0148</span>
        </div>
      </div>
      <div class="web-band">
        <svg class="globe-icon" viewBox="0 0 34 34" aria-hidden="true" fill="none" stroke="#ffffff" stroke-width="2">
          <circle cx="17" cy="17" r="15"/>
          <ellipse cx="17" cy="17" rx="7" ry="15"/>
          <line x1="17" y1="2" x2="17" y2="32"/>
          <line x1="2" y1="17" x2="32" y2="17"/>
          <path d="M5 9.5h24M5 24.5h24"/>
        </svg>
        <span class="web-address">www.oakmerekitchens.net</span>
      </div>
      <div class="showroom-photo" role="img" aria-label="Photo of a bright showroom kitchen with white cabinets, wood accents, pendant lights and an island with bar stools"></div>
    </section>
  </main>
</body>
</html>
```